Kelvo.cn needs pages to be re-designed

www.kelvo.cn is our current new site which was launched in April.
We're a financial services website in the crowdfunding space in China to connect borrower's and lender's.

test.kelvo.cn is our test site
u: test
p: fogpine
http://test.kelvo.cn/
http://test.kelvo.cn/user/accounts/new_lender
http://test.kelvo.cn/user/accounts/new_borrower
http://test.kelvo.cn/introductions/protection
http://test.kelvo.cn/introductions
http://test.kelvo.cn/introductions/kelvo_admin
http://test.kelvo.cn/introductions/contact
Some of the pages have pop-ups in the bloc's of the pages. Please click the links, to see more content.

User's currently criticize the website for being:
- Too Western looking
- Too simple, too little content
- Content NOT in the pop-ups are too simple
- Pictures are too big and too much blank space
- Relevant information is not there when needed
- The pictures are too generic

What we would like to do is re-design those pages with the same color scheme and style to be more compelling, efficient, non-intimidating and easy-to-use. Our audience is Ages 25-35 predominantly male investors.
We are looking for more ideas to make the content match the style, while bridging western and chinese design. Our ultimate goal is to increase registrants to the website and highlight our core competitive advantages.

Some competitors websites are:
www.tobumix.com
www.fesca.com
www.zwqvolt.com

Reason: Not enough good designs that follow the prompt. Same style, better information layout!

Reason: Still have not received a design we're satisfied with

Reason: WE DONT WANT A COMPLETE REDESIGN OF PAGES . KEEP THE EXACT SAME COLOR AND STYLE - WE WANT CONTENT RE-DESIGN! THE BLOCS ARE TOO SIMPLE - WE WANT MORE CONTENT INSIDE.

Reason: no new designs

Reason: no new designs

Reason: other non-registered pages need to be re-designed

```html
<!DOCTYPE html>
<html lang="zh-CN">
<head>
<meta charset="utf-8">
<title>Kelvo.cn 首页</title>
<link rel="stylesheet" href="https://fonts.googleapis.com/css2?family=Noto+Sans+SC:wght@300;400;500;700&family=Raleway:wght@300;400;600&display=swap">
<style>
:root{
  --green:#5cb82e;
  --green-dark:#4a9e22;
  --blue:#2a8dd4;
  --blue-light:#2fa3dc;
  --ink:#333333;
  --ink-soft:#666666;
  --muted:#999999;
  --line:#e2e2e2;
  --dark:#3a3a3a;
  --footer:#323232;
  --paper:#ffffff;
  --tint:#f2f4ee;
  --gray-band:#ececec;
  --orange:#f6a24b;
  --yellow:#f6d64c;
  --red:#e7564b;
  --purple:#9e7ba0;
}
*{box-sizing:border-box;margin:0;padding:0}
html,body{width:1200px;height:2837px;overflow:hidden}
body{font-family:"Noto Sans SC",sans-serif;color:var(--ink);background:var(--paper);position:relative;font-size:13px}
.abs{position:absolute}

/* header */
.site-header{position:absolute;left:0;top:0;width:1200px;height:90px;background:var(--paper);border-bottom:1px solid var(--line)}
.brand{position:absolute;left:100px;top:22px;display:flex;align-items:center;gap:10px}
.brand-dot{width:44px;height:44px;border-radius:50%;background:var(--green)}
.brand-name{font-size:24px;font-weight:700;color:var(--green)}
.main-nav{position:absolute;right:95px;top:33px;display:flex;gap:34px;font-size:14px;color:var(--ink)}
.main-nav span{display:flex;align-items:center;gap:6px}

/* hero */
.hero{position:absolute;left:0;top:90px;width:1200px;height:478px;overflow:hidden}
.hero-bg{position:absolute;inset:0;background:linear-gradient(180deg,#f4f6f8 0%,#e4ebf1 55%,#d2dde6 100%)}
.hero-photo{position:absolute;left:0;top:20px;width:500px;height:400px;background:radial-gradient(ellipse at 55% 45%,#8fb86a 0%,#c9b69c 45%,rgba(228,235,241,0) 75%)}
.slider-dots{position:absolute;right:70px;top:22px;display:flex;gap:5px}
.slider-dots i{width:12px;height:12px;border-radius:50%;background:#cfd6dc;border:1px solid #b9c2c9}
.slider-dots i.on{background:#9fa9b2}
.hero-title{position:absolute;left:535px;top:100px;width:580px;font-family:"Raleway",sans-serif;font-weight:400;font-size:37px;line-height:44px;color:#222}
.hero-text{position:absolute;left:535px;top:198px;width:570px;font-family:"Raleway",sans-serif;font-size:18px;line-height:24px;color:#333}
.read-more{position:absolute;left:535px;top:308px;width:240px;height:46px;border-radius:23px;background:var(--green);color:#fff;font-family:"Raleway",sans-serif;font-weight:600;font-size:16px;display:flex;align-items:center;padding-left:74px}
.read-more::before{content:"";position:absolute;left:-2px;top:-4px;width:54px;height:54px;border-radius:50%;background:#fff;border:3px solid var(--green)}
.hero-arrow{position:absolute;right:88px;top:210px}
.media-row{position:absolute;left:100px;top:420px;width:1000px;display:flex;justify-content:space-between;align-items:center}
.media-row i{display:block;height:28px;background:#8b9199;opacity:.55;border-radius:2px}

/* feature tabs */
.feature-tabs{position:absolute;left:0;top:568px;width:1200px;height:58px;display:flex;background:var(--dark)}
.feature-tabs div{flex:1;display:flex;align-items:center;justify-content:center;gap:10px;color:#fff;font-size:24px}
.feature-tabs .active{background:var(--green)}
.tab-note{position:absolute;left:0;top:626px;width:1200px;height:30px;background:var(--tint);text-align:center;line-height:30px;font-size:10px;color:var(--green-dark)}

/* notice */
.notice{position:absolute;left:0;top:656px;width:1200px;height:56px;border-bottom:1px solid var(--line)}
.notice-title{position:absolute;left:175px;top:18px;font-size:14px}
.notice-date{position:absolute;left:825px;top:18px;font-size:14px}
.notice-more{position:absolute;left:928px;top:14px;width:100px;height:28px;border:1px solid var(--blue);color:var(--blue);border-radius:14px;font-size:12px;display:flex;align-items:center;justify-content:center}
.ticker{position:absolute;left:0;top:712px;width:1200px;height:56px;background:var(--tint);display:flex;align-items:center;padding-left:130px;gap:46px;font-size:15px;color:var(--ink)}
.ticker b{font-weight:400;color:var(--green)}

/* stats */
.stats{position:absolute;left:0;top:770px;width:1200px;height:100px;background:#fafafa;border-bottom:1px solid var(--line)}
.stat{position:absolute;top:26px;padding-left:10px}
.stat + .stat{border-left:1px solid #ccc}
.stat strong{display:block;font-weight:400;font-size:26px;color:var(--blue);line-height:30px}
.stat small{font-size:9px;color:var(--muted)}
.start-invest{position:absolute;left:830px;top:28px;width:196px;height:48px;border-radius:24px;background:var(--blue);color:#fff;font-size:22px;font-weight:500;display:flex;align-items:center;padding-left:64px}
.start-invest::before{content:"";position:absolute;left:4px;top:4px;width:40px;height:40px;border-radius:50%;background:#fff}

/* listing */
.listing-title{position:absolute;left:175px;top:900px;font-size:24px;color:var(--green);font-weight:500}
.listing{position:absolute;left:175px;top:948px;width:852px;border-collapse:collapse;font-size:12px;color:var(--muted)}
.listing th{height:44px;background:#ececec;text-align:left;font-weight:500;color:var(--ink);font-size:13px;padding-left:10px}
.listing td{height:51px;border-bottom:1px solid var(--line);padding-left:10px}
.grade{display:inline-flex;gap:6px;align-items:center}
.grade i{width:24px;height:24px;border-radius:50%;background:var(--green);color:#fff;font-style:normal;font-weight:700;font-size:13px;display:inline-flex;align-items:center;justify-content:center}
.grade i.transfer{background:#7fb3e3;font-weight:400;font-size:11px}
.progress{display:inline-flex;align-items:center;gap:14px}
.lend-btn{width:90px;height:28px;border-radius:14px;background:var(--blue);color:#fff;font-size:12px;display:inline-flex;align-items:center;justify-content:center}
.lend-btn.done{background:#c6c6c6}
.tooltip{position:absolute;left:378px;top:966px;width:186px;height:118px;background:#fff;box-shadow:0 2px 8px rgba(0,0,0,.22);padding:10px 12px;font-size:8px;line-height:11px;color:#888}
.tooltip .mark{position:absolute;left:14px;bottom:12px;width:80px;height:18px;background:#d6e6cf}

/* fixed products */
.fixed{position:absolute;left:0;top:1356px;width:1200px;height:120px;display:flex}
.fixed-head{width:275px;background:var(--blue-light);color:#fff;padding:20px 0 0 115px;font-size:24px}
.fixed-head em{display:block;margin-top:12px;width:70px;border-top:3px solid #fff;box-shadow:0 9px 0 0 #fff,0 18px 0 0 #fff}
.product{flex:1;padding:12px 0 0 22px;color:#222}
.product .top{display:flex;align-items:baseline;gap:14px;font-size:14px}
.product .top strong{font-size:26px;font-weight:700}
.product .mid{margin-top:8px;font-size:14px}
.product .go{margin-top:12px;width:90px;height:26px;background:#3d3d3d;color:#fff;border-radius:13px;font-size:12px;display:flex;align-items:center;justify-content:center}
.p-orange{background:var(--orange)}.p-yellow{background:var(--yellow)}.p-red{background:var(--red)}.p-purple{background:var(--purple)}

/* steps */
.steps{position:absolute;left:0;top:1476px;width:1200px;height:264px;background:var(--gray-band)}
.step{position:absolute;top:40px;width:300px;text-align:center}
.step .ring{width:100px;height:100px;margin:0 auto;border-radius:50%;background:#fff;display:flex;align-items:center;justify-content:center}
.step h3{margin-top:30px;font-size:25px;font-weight:500;color:#222}
.step p{margin-top:6px;font-size:12px;color:var(--ink-soft)}
.step.blue h3,.step.blue p{color:var(--blue)}

/* trust */
.trust{position:absolute;left:0;top:1740px;width:1200px;height:222px;background:#fff}
.trust-title{position:absolute;left:325px;top:60px;font-size:20px;color:var(--blue)}
.trust-text{position:absolute;left:325px;top:92px;width:270px;font-size:10px;line-height:15px;color:var(--ink-soft)}
.trust-more{position:absolute;left:325px;top:156px;width:96px;height:24px;background:#888;color:#fff;border-radius:12px;font-size:12px;display:flex;align-items:center;justify-content:center}
.trust-divider{position:absolute;left:596px;top:18px;width:6px;height:186px;background:linear-gradient(90deg,#d8d8d8,#fff)}
.partner-marks{position:absolute;left:700px;top:30px;display:flex;gap:16px;align-items:center}
.partner-marks i{display:block;height:46px;border-radius:3px}
.trust-note{position:absolute;left:640px;top:148px;width:360px;text-align:center;font-size:11px;line-height:15px;color:#222}
.trust-links{position:absolute;left:745px;top:182px;font-size:11px;color:var(--blue);display:flex;gap:22px}

/* service */
.service{position:absolute;left:0;top:1962px;width:1200px;height:288px;background:var(--green);color:#fff}
.service h2{position:absolute;left:205px;top:84px;font-size:25px;font-weight:500}
.service p{position:absolute;left:205px;top:132px;width:530px;font-size:12px;line-height:17px}
.service a{position:absolute;left:205px;top:198px;font-size:12px;color:#fff;text-decoration:underline}
.service .badge{position:absolute;left:822px;top:42px;width:210px;height:210px;border-radius:50%;background:radial-gradient(circle,#ffffff 0%,#f3f8ef 78%,#e6f1dd 100%)}

/* news */
.news{position:absolute;left:0;top:2250px;width:1200px;height:262px;display:flex}
.news section{flex:1;position:relative}
.news .media{background:#ebebeb}
.news .official{background:#f4f4f4}
.news h2{position:absolute;top:46px;font-size:24px;font-weight:500;color:var(--green)}
.news ul{position:absolute;top:86px;list-style:none;font-size:11px;line-height:22px;color:#222}
.news li::before{content:"";display:inline-block;width:6px;height:6px;border-radius:50%;background:#222;margin-right:10px;vertical-align:middle}
.news li.hot{color:#7fb3e3;text-decoration:underline}
.news .more{position:absolute;top:210px;width:70px;height:26px;background:#777;color:#fff;border-radius:13px;font-size:12px;display:flex;align-items:center;justify-content:center}

/* partners */
.partners{position:absolute;left:0;top:2512px;width:1200px;height:108px;background:#fff}
.partners h4{position:absolute;left:175px;top:14px;font-size:12px;font-weight:500}
.partner-row{position:absolute;left:205px;top:46px;display:flex;gap:34px;align-items:center}
.partner-row i{display:block;height:28px;background:#c9ced6;border-radius:2px}

/* footer */
.site-footer{position:absolute;left:0;top:2620px;width:1200px;height:170px;background:var(--footer);color:#fff;font-size:12px}
.foot-links{position:absolute;left:175px;top:16px;display:flex;gap:14px}
.foot-friends{position:absolute;left:175px;top:42px}
.foot-service{position:absolute;left:175px;top:70px;display:flex;align-items:center;gap:10px}
.foot-service i{width:18px;height:18px;border-radius:50%;background:#999}
.foot-service .chat{margin-left:14px;width:98px;height:26px;border-radius:13px;background:#1f1f1f;display:flex;align-items:center;justify-content:center}
.hotline{position:absolute;right:175px;top:14px;text-align:right}
.hotline strong{display:block;font-size:26px;font-weight:500;margin-top:6px;line-height:30px}
.hotline small{font-size:9px;color:#bbb}
.cert-row{position:absolute;left:270px;top:122px;width:660px;display:flex;justify-content:space-between}
.cert-row i{display:block;height:28px;background:#6a6a6a;border-radius:2px}
.copyright{position:absolute;left:0;top:2790px;width:1200px;height:47px;background:#f0f0f0}
.copyright p{position:absolute;left:175px;top:16px;font-size:9px;color:#888}
.copyright .brand-mini{position:absolute;right:180px;top:10px;display:flex;align-items:center;gap:6px;color:var(--green);font-weight:700;font-size:16px}
.copyright .brand-mini i{width:24px;height:24px;border-radius:50%;background:var(--green)}
</style>
</head>
<body>

<header class="site-header">
  <div class="brand"><span class="brand-dot"></span><span class="brand-name">Kelvo.cn</span></div>
  <nav class="main-nav">
    <span><svg width="14" height="16" viewBox="0 0 14 16"><path d="M7 1 13 3v5c0 4-3 6-6 7-3-1-6-3-6-7V3z" fill="none" stroke="#444" stroke-width="1.5"/></svg>安全</span>
    <span><svg width="14" height="16" viewBox="0 0 14 16"><path d="M3 2l4 5 4-5M7 7v8M3 9h8M3 12h8" fill="none" stroke="#444" stroke-width="1.5"/></svg>投资</span>
    <span><svg width="14" height="16" viewBox="0 0 14 16"><rect x="2" y="7" width="10" height="8" fill="none" stroke="#444" stroke-width="1.5"/><path d="M4 7V4a3 3 0 0 1 6 0v3" fill="none" stroke="#444" stroke-width="1.5"/></svg>贷款</span>
    <span><svg width="14" height="16" viewBox="0 0 14 16"><circle cx="7" cy="5" r="3" fill="#444"/><path d="M1 15c0-4 3-6 6-6s6 2 6 6z" fill="#444"/></svg>登录 ▾</span>
  </nav>
</header>

<section class="hero">
  <div class="hero-bg" role="img" aria-label="浅色虚化的城市天际线背景照片"></div>
  <div class="hero-photo" role="img" aria-label="双手捧着长成上升箭头形状的绿色植物的照片"></div>
  <div class="slider-dots"><i class="on"></i><i></i><i></i><i></i></div>
  <h1 class="hero-title">LOREM IPSUM DOLOR SIT AMET, CONSECTETUER ...</h1>
  <p class="hero-text">Ut wisi enim ad minim veniam, quis nostrud exerci tation ullamcorper suscipit lobortis nisl ut aliquip ex ea commodo consequat.</p>
  <div class="read-more">READ MORE</div>
  <svg class="hero-arrow" width="16" height="28" viewBox="0 0 16 28"><path d="M2 2l12 12L2 26" fill="none" stroke="#555" stroke-width="2"/></svg>
  <div class="media-row">
    <i style="width:62px"></i><i style="width:62px"></i><i style="width:58px"></i><i style="width:64px"></i><i style="width:110px"></i><i style="width:86px"></i><i style="width:74px"></i><i style="width:130px"></i><i style="width:70px"></i><i style="width:32px"></i>
  </div>
</section>

<div class="feature-tabs">
  <div><svg width="34" height="26" viewBox="0 0 34 26"><rect x="0" y="18" width="5" height="8" fill="#fff"/><rect x="8" y="13" width="5" height="13" fill="#fff"/><rect x="16" y="8" width="5" height="18" fill="#fff"/><rect x="24" y="2" width="5" height="24" fill="#fff"/></svg>高回报</div>
  <div class="active"><svg width="26" height="30" viewBox="0 0 26 30"><path d="M13 1 25 5v9c0 8-6 13-12 15C7 27 1 22 1 14V5z" fill="#fff"/><path d="M13 5v21c-4-2-8-6-8-12V8z" fill="#5cb82e"/></svg>安全</div>
  <div><svg width="28" height="28" viewBox="0 0 28 28"><circle cx="14" cy="14" r="12" fill="none" stroke="#fff" stroke-width="2.5"/><path d="M14 6v8h7" fill="none" stroke="#fff" stroke-width="2.5"/></svg>高效</div>
</div>
<div class="tab-note">凯沃贷是一个安全、高效、透明的投资平台。</div>

<div class="notice">
  <span class="notice-title">凯沃贷网 邀请有返利啦</span>
  <span class="notice-date">2014-06-05</span>
  <span class="notice-more">更多公告</span>
</div>
<div class="ticker">
  <span><b>成功贷款</b> 10000元 年利率 15.0%</span>
  <span><b>成功投资</b> 2000元 年利率 15.0%</span>
  <span><b>成功贷款</b> 20000元 年利率 15.0%</span>
  <span><b>成功投资</b> 3000元 年利率 15.0%</span>
</div>

<div class="stats">
  <div class="stat" style="left:165px;border:0"><strong>¥56573</strong><small>资金保障</small></div>
  <div class="stat" style="left:310px"><strong>14.68%</strong><small>平均收益率</small></div>
  <div class="stat" style="left:465px"><strong>11.8月</strong><small>平均期限</small></div>
  <div class="start-invest">开始投资</div>
</div>

<h2 class="listing-title">投资列表</h2>
<table class="listing">
  <thead><tr><th style="width:118px">借款标题</th><th style="width:165px">信用等级</th><th style="width:130px">年利率</th><th style="width:110px">金额</th><th style="width:100px">期限</th><th style="width:130px">进度</th><th></th></tr></thead>
  <tbody>
    <tr><td>fafafa</td><td><span class="grade"><i>S</i><svg width="20" height="22" viewBox="0 0 20 22"><path d="M10 1 19 4v7c0 5-4 9-9 10-5-1-9-5-9-10V4z" fill="#5cb82e"/></svg></span></td><td>15.0%</td><td>30000元</td><td>13个月</td><td><span class="progress"><svg width="24" height="24"><circle cx="12" cy="12" r="12" fill="#e6e6e6"/></svg>0.0%</span></td><td><span class="lend-btn">开始出借</span></td></tr>
    <tr><td>fafafa</td><td><span class="grade"><i>S</i><svg width="20" height="22" viewBox="0 0 20 22"><path d="M10 1 19 4v7c0 5-4 9-9 10-5-1-9-5-9-10V4z" fill="#5cb82e"/></svg></span></td><td>12.0%</td><td>12000元</td><td>4个月</td><td><span class="progress"><svg width="24" height="24"><circle cx="12" cy="12" r="12" fill="#e6e6e6"/></svg>0.0%</span></td><td><span class="lend-btn">开始出借</span></td></tr>
    <tr><td>fafafa</td><td><span class="grade"><i>B</i><svg width="20" height="22" viewBox="0 0 20 22"><path d="M10 1 19 4v7c0 5-4 9-9 10-5-1-9-5-9-10V4z" fill="#5cb82e"/></svg><i class="transfer">转</i></span></td><td>15.0%</td><td>30000元</td><td>0个月</td><td><span class="progress"><svg width="24" height="24"><circle cx="12" cy="12" r="12" fill="#e6e6e6"/></svg>0.0%</span></td><td><span class="lend-btn">开始出借</span></td></tr>
    <tr><td>fafafa</td><td><span class="grade"><i>B</i><svg width="20" height="22" viewBox="0 0 20 22"><path d="M10 1 19 4v7c0 5-4 9-9 10-5-1-9-5-9-10V4z" fill="#5cb82e"/></svg><i class="transfer">转</i></span></td><td>15.0%</td><td>30000元</td><td>5个月</td><td><span class="progress"><svg width="24" height="24"><circle cx="12" cy="12" r="12" fill="#e6e6e6"/></svg>0.0%</span></td><td><span class="lend-btn">开始出借</span></td></tr>
    <tr><td>fafafa</td><td><span class="grade"><i>A</i><svg width="20" height="22" viewBox="0 0 20 22"><path d="M10 1 19 4v7c0 5-4 9-9 10-5-1-9-5-9-10V4z" fill="#5cb82e"/></svg></span></td><td>15.0%</td><td>30000元</td><td>12个月</td><td><span class="progress"><svg width="24" height="24"><circle cx="12" cy="12" r="12" fill="#e6e6e6"/><path d="M12 0a12 12 0 0 1 0 24z" fill="#5cb82e"/></svg>50.0%</span></td><td><span class="lend-btn done">开始出借</span></td></tr>
    <tr><td>fafafa</td><td><span class="grade"><i>A</i><svg width="20" height="22" viewBox="0 0 20 22"><path d="M10 1 19 4v7c0 5-4 9-9 10-5-1-9-5-9-10V4z" fill="#5cb82e"/></svg></span></td><td>15.0%</td><td>30000元</td><td>0个月</td><td><span class="progress"><svg width="24" height="24"><circle cx="12" cy="12" r="12" fill="#5cb82e"/></svg>100.0%</span></td><td><span class="lend-btn done">开始出借</span></td></tr>
  </tbody>
</table>
<div class="tooltip">该借款已由合作保险机构承保，本金与利息均受保障，出借人可在到期后按时收回全部资金，详情请见保障说明页面。
  <span class="mark"></span>
</div>

<div class="fixed">
  <div class="fixed-head">固定产品<em></em></div>
  <div class="product p-orange"><div class="top">3个月回报率<strong>10.0%</strong></div><div class="mid">剩下9笔，每笔1.0万元</div><div class="go">现在投资</div></div>
  <div class="product p-yellow"><div class="top">6个月回报率<strong>11.0%</strong></div><div class="mid">剩下9笔，每笔1.0万元</div><div class="go">现在投资</div></div>
  <div class="product p-red"><div class="top">9个月回报率<strong>12.0%</strong></div><div class="mid">剩下9笔，每笔1.0万元</div><div class="go">现在投资</div></div>
  <div class="product p-purple"><div class="top">12个月回报率<strong>13.0%</strong></div><div class="mid">剩下9笔，每笔1.0万元</div><div class="go">现在投资</div></div>
</div>

<section class="steps">
  <div class="step" style="left:152px">
    <div class="ring"><svg width="44" height="48" viewBox="0 0 44 48"><circle cx="22" cy="27" r="18" fill="none" stroke="#333" stroke-width="3"/><path d="M22 27V16M17 4h10M22 4v5" fill="none" stroke="#333" stroke-width="3"/></svg></div>
    <h3>3分钟内即可完成投资</h3><p>注册、验证身份和电子邮件</p>
  </div>
  <div class="step blue" style="left:450px">
    <div class="ring"><svg width="48" height="44" viewBox="0 0 48 44"><path d="M24 2 46 14H2z" fill="#2a8dd4"/><rect x="6" y="17" width="5" height="18" fill="#2a8dd4"/><rect x="16" y="17" width="5" height="18" fill="#2a8dd4"/><rect x="27" y="17" width="5" height="18" fill="#2a8dd4"/><rect x="37" y="17" width="5" height="18" fill="#2a8dd4"/><rect x="2" y="38" width="44" height="5" fill="#2a8dd4"/></svg></div>
    <h3>充值账户</h3><p>支持更多银行</p>
  </div>
  <div class="step" style="left:746px">
    <div class="ring"><svg width="40" height="48" viewBox="0 0 40 48"><path d="M16 46V18a4 4 0 0 1 8 0v12l10 3c3 1 4 3 3 6l-3 7z" fill="none" stroke="#333" stroke-width="3"/><path d="M20 2v6M8 8l4 4M32 8l-4 4M4 18h6M30 18h6" stroke="#333" stroke-width="2.5"/></svg></div>
    <h3>选择您的投资方式</h3><p>手动投资、固定产品或快速投资</p>
  </div>
</section>

<section class="trust">
  <svg class="abs" style="left:190px;top:50px" width="120" height="130" viewBox="0 0 120 130"><polyline points="8,60 38,36 70,50 110,8" fill="none" stroke="#2a8dd4" stroke-width="7" stroke-linejoin="round"/><circle cx="8" cy="60" r="8" fill="#2a8dd4"/><circle cx="38" cy="36" r="8" fill="#2a8dd4"/><circle cx="70" cy="50" r="8" fill="#2a8dd4"/><circle cx="110" cy="8" r="8" fill="#2a8dd4"/><rect x="20" y="82" width="22" height="48" fill="#555"/><rect x="52" y="66" width="22" height="64" fill="#555"/><rect x="84" y="48" width="22" height="82" fill="#555"/></svg>
  <h3 class="trust-title">每年回报率10%-15%</h3>
  <p class="trust-text">凯沃贷采用可持续的方式保持稳健运营，我们关注借款人的长期健康状况，以帮助投资者获得高于平均水平的回报。</p>
  <div class="trust-more">了解详情</div>
  <div class="trust-divider"></div>
  <div class="partner-marks">
    <i style="width:86px;background:#c8dcc0"></i>
    <i style="width:96px;background:#e3cfd0"></i>
  </div>
  <svg class="abs" style="left:640px;top:92px" width="360" height="50" viewBox="0 0 360 50"><path d="M20 8 34 13v10c0 9-7 14-14 16-7-2-14-7-14-16V13z" fill="#555"/><path d="M40 26h270" stroke="#888" stroke-width="1.5"/><path d="M310 26 300 21v10z" fill="#888"/><path d="M332 2 344 6v8c0 7-6 11-12 13-6-2-12-6-12-13V6z" fill="#5cb82e"/><path d="M332 24 344 28v8c0 7-6 11-12 13-6-2-12-6-12-13v-8z" fill="#5cb82e"/></svg>
  <p class="trust-note">我们是唯一一与中国及澳大利亚保险公司合作的P2P平台<br>提供最安全的理财保障</p>
  <div class="trust-links"><span>了解合作</span><span>了解安全</span></div>
</section>

<section class="service">
  <h2>高效服务，让您满意</h2>
  <p>2天内获得贷款或3分钟内完成投资，您可以随时随地了解您的资金流向，我们是一个快速高效的平台，让您自始自终拥有完全控制权。</p>
  <a>了解详情</a>
  <div class="badge" role="img" aria-label="白色圆形徽章插图：代表安全账户的人物与锁孔图形"></div>
</section>

<section class="news">
  <section class="media">
    <h2 style="left:205px">媒体报道</h2>
    <ul style="left:205px">
      <li class="hot">这就是为什么人们把一个简单的例子</li>
      <li>这就是为什么人们把</li>
      <li>这就是为什么人们把一个简单的例子作为例子</li>
      <li>这就是为什么人们把一个简单的例子</li>
      <li>这就是为什么人们把一个简单个简单的例子</li>
    </ul>
    <div class="more" style="left:205px">更多&gt;</div>
  </section>
  <section class="official">
    <h2 style="left:45px">官方公告</h2>
    <ul style="left:45px">
      <li>这就是为什么人们把一个简单的例子</li>
      <li>这就是为什么人们把一个简单的例子</li>
      <li>这就是为什么人们把一个简单的例子作为例子的例子</li>
      <li>这就是为什么人们把一个简单的例子</li>
      <li>这就是为什么人们把一个简单的例子</li>
    </ul>
    <div class="more" style="left:45px">更多&gt;</div>
  </section>
</section>

<section class="partners">
  <h4>合作伙伴</h4>
  <div class="partner-row">
    <i style="width:112px"></i><i style="width:128px"></i><i style="width:150px"></i><i style="width:40px"></i><i style="width:78px"></i><i style="width:150px"></i>
  </div>
</section>

<footer class="site-footer">
  <div class="foot-links"><span>投资</span><span>贷款</span><span>安全</span><span>媒体</span><span>合作</span><span>关于我们</span><span>联系我们</span><span>加入我们</span><span>帮助中心</span></div>
  <div class="foot-friends">友情链接：贷友之家　理财天窗　借贷俱乐部</div>
  <div class="foot-service">客户服务：<i></i><i></i><i></i><i></i><span class="chat">在线客服</span></div>
  <div class="hotline">客服电话<strong>400-820-5566</strong><small>周一至周日 9:00-18:00</small></div>
  <div class="cert-row"><i style="width:30px"></i><i style="width:70px"></i><i style="width:86px"></i><i style="width:76px"></i><i style="width:76px"></i><i style="width:90px"></i></div>
</footer>
<div class="copyright">
  <p>Copyright © 2014 京ICP备20481736号 版权所有 | 北京凯沃信息服务有限公司</p>
  <div class="brand-mini"><i></i>Kelvo.cn</div>
</div>

</body>
</html>
```